New Internet Service provider for regional or isolated businesses

I'm looking for a logo and basic information website for an Internet company - "Quill Ridge Networks". This new company will be providing specialised Internet connectivity for isolated areas or where connectivity is too expensive for one business.
i.e Linking Workplaces as one for faster, cheaper Web access.
3 Types of Pages
1. Home Page
2. Content Page templates
3. More Information Form
1. Contact Name. 2. Business Address. 3. Business Phone Number. 4. Mobile Phone. 5. Number of Staff 6. Current Internet connection . 7. Speed 8. Comments ?
Web Pages
**Quill Ridge Networks **
Linking Workplaces as one for faster Web access
Who is Quill Ridge Networks ?
How do we work ?
Which carriers ?
Technologies Used ?
Contact details
Check my address now ?
(Form)
Our company will be using Fibre and Microwave/Radio technology to connect remote businesses to high speed Internet
Target Market(s)
Business customers with minimum 10 staff outside metropolitan areas
Industry/Entity Type
Internet Service Provider
Coding
Coded - Design and coding required
Number of Pages Required
3 page
Requirements
Must have
- 3 Types of Pages
- 1. Home Page
- 2. Content Page templates (See above)
- 3. "More Information" Form
- 1. Contact Name. 2. Business Address. 3. Business Phone Number. 4. Mobile Phone. 5. Number of Staff 6.Current Internet connection . 7. Speed 8.Comments ?
Nice to have
- Pictures of fibre optics, radio towers, stock photos of businesses / PC's
- Some ideas on the companies we will be using (I am looking for something similar in my website).
- In order of preference
- 1. www.travenlo.com.au
- 2. www.pomrika.com,au
- 3.www.fendoly.com.au

```html
<!DOCTYPE html>
<html lang="en">
<head>
<meta charset="utf-8">
<title>Quill Ridge Networks</title>
<link rel="stylesheet" href="https://fonts.googleapis.com/css2?family=Lato:wght@400;700&family=Mulish:wght@600;700&display=swap">
<style>
  :root {
    --bar-dark: #333333;
    --ink: #333333;
    --brand-blue: #2f72b8;
    --white: #ffffff;
    --navy-deep: #141d33;
    --navy-mid: #2b3f6b;
    --navy-light: #6f86b5;
    --band: rgba(18, 22, 32, 0.78);
    --placeholder: #9a9a9a;
    --social-1: #0d5a97;
    --social-2: #1686c6;
    --social-3: #17b3d3;
    --social-4: #df533d;
  }
  * { box-sizing: border-box; margin: 0; padding: 0; }
  html, body { width: 1200px; height: 711px; overflow: hidden; background: var(--white); }
  body { font-family: "Lato", Arial, sans-serif; color: var(--ink); position: relative; }
  .container { position: absolute; left: 99px; width: 1002px; }

  .topbar { position: absolute; top: 0; left: 0; width: 1200px; height: 34px; background: var(--bar-dark); }
  .topbar .container { height: 34px; display: flex; align-items: stretch; }
  .contact-item { display: flex; align-items: center; gap: 7px; padding: 0 10px 0 7px; color: var(--white); font-size: 12px;
    border-left: 1px solid #555; border-right: 1px solid #555; }
  .contact-item + .contact-item { border-left: none; }
  .contact-item.phone { font-weight: 700; font-size: 13px; }
  .social-squares { margin-left: auto; display: flex; gap: 2px; }
  .social-squares span { width: 26px; height: 34px; display: block; }
  .social-squares span:nth-child(1) { background: var(--social-1); }
  .social-squares span:nth-child(2) { background: var(--social-2); }
  .social-squares span:nth-child(3) { background: var(--social-3); }
  .social-squares span:nth-child(4) { background: var(--social-4); }

  .site-header { position: absolute; top: 34px; left: 0; width: 1200px; height: 95px; background: var(--white); }
  .brand { position: absolute; top: 18px; left: 0; display: flex; align-items: center; gap: 10px; }
  .brand-dot { width: 54px; height: 54px; border-radius: 50%; background: var(--brand-blue); }
  .brand-name { font-family: "Lato", Arial, sans-serif; font-weight: 700; font-size: 23px; line-height: 26px;
    letter-spacing: 1.5px; text-transform: uppercase; color: var(--ink); }
  .main-nav { position: absolute; top: 30px; right: 0; display: flex; align-items: center; }
  .main-nav a { font-size: 15px; font-weight: 700; color: var(--ink); text-decoration: none; margin-left: 28px; }
  .main-nav a.active { color: var(--brand-blue); border: 1px solid var(--brand-blue); padding: 8px 14px; margin-left: 0; }

  .hero { position: absolute; top: 129px; left: 0; width: 1200px; height: 531px;
    background:
      radial-gradient(ellipse 420px 260px at 300px 170px, rgba(150,175,220,0.55), transparent 70%),
      radial-gradient(ellipse 380px 230px at 780px 280px, rgba(120,140,190,0.45), transparent 70%),
      linear-gradient(110deg, var(--navy-mid) 0%, var(--navy-light) 45%, var(--navy-mid) 70%, var(--navy-deep) 100%); }
  .hero-title { position: absolute; top: 336px; left: 0; width: 1200px; text-align: center;
    font-family: "Mulish", Arial, sans-serif; font-weight: 700; font-size: 37px; color: var(--white);
    text-transform: capitalize; text-shadow: 2px 3px 4px rgba(0,0,0,0.6); }

  .address-check { position: absolute; top: 420px; left: 0; width: 1200px; height: 111px; background: var(--band); }
  .address-check .container { top: 0; height: 111px; }
  .address-check h2 { position: absolute; left: 0; top: 26px; font-family: "Mulish", Arial, sans-serif; font-weight: 600;
    font-size: 23px; line-height: 27px; color: var(--white); }
  .field { position: absolute; top: 37px; height: 38px; background: var(--white); border: none;
    font-family: "Lato", Arial, sans-serif; font-size: 14px; color: var(--placeholder); padding: 0 8px; line-height: 38px; }
  .field.address { left: 189px; width: 368px; }
  .field.zip { left: 595px; width: 283px; }
  .go-button { position: absolute; top: 37px; right: 0; width: 86px; height: 38px; border: 1px solid var(--white);
    color: var(--white); font-weight: 700; font-size: 14px; text-align: center; line-height: 36px; }

  .site-footer { position: absolute; top: 660px; left: 0; width: 1200px; height: 51px; background: var(--bar-dark); }
  .site-footer .container { height: 51px; display: flex; align-items: center; }
  .follow { display: flex; align-items: center; gap: 8px; color: var(--white); font-size: 17px; }
  .follow .label { margin-right: 2px; }
  .follow span.ring { width: 26px; height: 26px; border: 1.5px solid var(--white); border-radius: 50%; display: block; }
  .copyright { margin-left: auto; color: var(--white); font-size: 13px; }
</style>
</head>
<body>
  <div class="topbar">
    <div class="container">
      <div class="contact-item phone">
        <svg width="11" height="11" viewBox="0 0 24 24"><path fill="#3f8fd8" d="M6.6 10.8a15 15 0 0 0 6.6 6.6l2.2-2.2c.3-.3.7-.4 1-.2 1.1.4 2.3.6 3.6.6.6 0 1 .4 1 1V20c0 .6-.4 1-1 1A17 17 0 0 1 3 4c0-.6.4-1 1-1h3.5c.6 0 1 .4 1 1 0 1.3.2 2.5.6 3.6.1.3 0 .7-.2 1z"/></svg>
        (555) 014-2290
      </div>
      <div class="contact-item">
        <svg width="13" height="9" viewBox="0 0 26 18"><rect width="26" height="18" fill="#3f8fd8"/><path d="M0 0l13 10L26 0" fill="none" stroke="#333" stroke-width="2"/></svg>
        info@quillridgenet.com
      </div>
      <div class="social-squares"><span></span><span></span><span></span><span></span></div>
    </div>
  </div>

  <header class="site-header">
    <div class="container">
      <div class="brand">
        <div class="brand-dot"></div>
        <div class="brand-name">Quill Ridge<br>Networks</div>
      </div>
      <nav class="main-nav">
        <a class="active" href="#">Home</a>
        <a href="#">Who We Are</a>
        <a href="#">Carriers We Use</a>
        <a href="#">Technologies Used</a>
        <a href="#">Contact Us</a>
      </nav>
    </div>
  </header>

  <section class="hero" role="img" aria-label="Photo of glowing fibre optic strands and network cable connectors">
    <h1 class="hero-title">Linking Workplaces as one for faster Web access</h1>
    <div class="address-check">
      <div class="container">
        <h2>Check Your<br>Address Now</h2>
        <div class="field address">Enter Your Address</div>
        <div class="field zip">Enter Zip Code</div>
        <div class="go-button">GO</div>
      </div>
    </div>
  </section>

  <footer class="site-footer">
    <div class="container">
      <div class="follow">
        <span class="label">Follow Us:</span>
        <span class="ring"></span><span class="ring"></span><span class="ring"></span><span class="ring"></span>
      </div>
      <div class="copyright">Copyright © 2016 QUILL RIDGE NETWORKS. All Rights Reserved.</div>
    </div>
  </footer>
</body>
</html>
```